Plumber needs a business card

I need a new business card for my plumbing business. I dont have a logo at the moment but I want business cards that are simple but very professional. I want to look like
Name: Mitch Dorley
Address: (just make one up)
Phone: 0455 318 726
Email: mitch@dorleymail.com
Colors to use:
Blacks, blues, silvers

```html
<!DOCTYPE html>
<html lang="en">
<head>
<meta charset="utf-8">
<title>Mitch Dorley – Business Card</title>
<link rel="stylesheet" href="https://fonts.googleapis.com/css2?family=Lato:wght@400;700&display=swap">
<style>
  :root {
    --page-bg: #e4e2df;
    --frost-light: #f3f4f5;
    --frost-mid: #dfe3e7;
    --frost-edge: #cfd4d9;
    --ink-dark: #2f2f33;
    --accent-blue: #3f86cf;
    --accent-blue-deep: #2c6aa8;
    --panel-dark: #1f1c1e;
    --panel-dark-soft: #3a3537;
    --detail-text: #cbc3b7;
  }
  * { margin: 0; padding: 0; box-sizing: border-box; }
  html, body {
    width: 1200px;
    height: 970px;
    overflow: hidden;
    background: var(--page-bg);
    font-family: "Lato", sans-serif;
  }
  .business-card {
    position: absolute;
    left: 100px;
    top: 207px;
    width: 1000px;
    height: 556px;
    border-radius: 26px;
    overflow: hidden;
    background: linear-gradient(160deg, var(--frost-light) 0%, var(--frost-mid) 55%, var(--frost-edge) 100%);
    box-shadow: 0 18px 40px rgba(0,0,0,0.18), inset 0 0 0 1px rgba(255,255,255,0.6);
  }
  .card-shapes {
    position: absolute;
    inset: 0;
    width: 100%;
    height: 100%;
  }
  .identity {
    position: absolute;
    left: 97px;
    top: 176px;
  }
  .identity-name {
    font-weight: 700;
    font-size: 27px;
    letter-spacing: 0.3px;
    color: var(--ink-dark);
    text-transform: uppercase;
    line-height: 1.1;
  }
  .identity-title {
    font-weight: 400;
    font-size: 21px;
    color: var(--accent-blue);
    line-height: 1.3;
  }
  .contact-block {
    position: absolute;
    right: 81px;
    text-align: right;
    color: var(--detail-text);
    font-size: 21px;
    line-height: 31px;
    font-style: normal;
  }
  .contact-address { top: 297px; right: 123px; }
  .contact-lines { top: 416px; }
  .contact-line {
    display: flex;
    justify-content: flex-end;
    align-items: center;
    gap: 12px;
  }
  .contact-icon { width: 26px; height: 22px; flex: none; }
</style>
</head>
<body>
  <div class="business-card">
    <svg class="card-shapes" viewBox="0 0 1000 556" preserveAspectRatio="none" aria-hidden="true">
      <defs>
        <linearGradient id="panel-dark-fill" x1="0" y1="0" x2="1" y2="1">
          <stop offset="0" stop-color="var(--panel-dark)"/>
          <stop offset="0.6" stop-color="#2a2628"/>
          <stop offset="1" stop-color="var(--panel-dark-soft)"/>
        </linearGradient>
      </defs>
      <polygon class="accent-stripe" fill="var(--accent-blue)" points="560,0 578,0 398,556 380,556"/>
      <polygon class="dark-panel" fill="url(#panel-dark-fill)" points="600,0 1000,0 1000,556 420,556"/>
      <rect class="base-line" x="0" y="540" width="380" height="16" fill="var(--accent-blue-deep)"/>
    </svg>

    <div class="identity">
      <h1 class="identity-name">Mitch Dorley</h1>
      <p class="identity-title">Managing Director</p>
    </div>

    <address class="contact-block contact-address">
      Suite 123, Street name,<br>
      State, Zip 5555, Country
    </address>

    <div class="contact-block contact-lines">
      <div class="contact-line">
        <span>0455 318 726</span>
        <svg class="contact-icon" viewBox="0 0 26 22" aria-label="Phone">
          <path fill="var(--accent-blue)" d="M2,7 C2,3 7,2 13,2 C19,2 24,3 24,7 L24,9 L18,9 L18,6 L8,6 L8,9 L2,9 Z"/>
          <path fill="var(--accent-blue)" d="M7,10 L19,10 L23,20 L3,20 Z"/>
          <circle cx="13" cy="15" r="3" fill="var(--panel-dark)"/>
        </svg>
      </div>
      <div class="contact-line">
        <span>mitch@dorleymail.com</span>
        <svg class="contact-icon" viewBox="0 0 26 22" aria-label="Email">
          <rect x="2" y="3" width="22" height="16" rx="1.5" fill="var(--accent-blue)"/>
          <path d="M3,4 L13,12 L23,4" fill="none" stroke="var(--panel-dark)" stroke-width="1.6"/>
          <path d="M3,18 L10,10 M23,18 L16,10" fill="none" stroke="var(--panel-dark)" stroke-width="1.2"/>
        </svg>
      </div>
    </div>
  </div>
</body>
</html>
```